Classic Minimalistic Business Card

Design a classic, minimalistic Business Card. Please find inspiration in the attached Classic Minimalistic examples. My information:
Name: Glen Ovamir
Company: Ovamir Capital
Logo: OC
Address: 1470 N Thornwick Rd, Suite 210 | Geneva, IL 60134
Phone: 630-555-0192
Email: glenovamir@pvt.insure
Slogan: Building Strength Through Capital

Feel free to leave out any of the information above except my name.

I have selected Double-sided, but I am also open to Single-sided

Target Market(s)

22-70. income greater than 150k/year

Industry/Entity Type

Finance

Contact Information for Business Card

See Project Description

Requirements
Must have
• Ivory or "antiqued" background similar to the reference pictures

```html
<!DOCTYPE html>
<html lang="en">
<head>
<meta charset="utf-8">
<title>Ovamir Capital — Business Card</title>
<link rel="stylesheet" href="https://fonts.googleapis.com/css2?family=Josefin+Sans:wght@400;600&family=Yellowtail&display=block">
<style>
  :root {
    --backdrop-top: #e8e8e8;
    --backdrop-bottom: #c9c9c9;
    --card: #f3ead6;
    --card-edge: #e6d8bc;
    --ink: #2a1a0b;
    --ink-soft: #5a4128;
    --accent: #7a5a36;
  }
  * { margin: 0; padding: 0; box-sizing: border-box; }
  html, body { width: 865px; height: 1200px; overflow: hidden; }
  body {
    background: linear-gradient(180deg, var(--backdrop-top), var(--backdrop-bottom));
    font-family: "Josefin Sans", Arial, sans-serif;
    position: relative;
  }
  .card {
    position: absolute;
    left: 122px;
    width: 620px;
    height: 353px;
    background: radial-gradient(ellipse at center, var(--card) 55%, var(--card-edge) 100%);
    box-shadow: 2px 3px 6px rgba(0, 0, 0, 0.3);
    text-align: center;
    overflow: hidden;
  }
  .card--front { top: 232px; }
  .card--back { top: 615px; }

  .brand {
    position: absolute;
    left: 0; right: 0;
    color: var(--ink);
  }
  .brand__name {
    display: inline-flex;
    align-items: center;
    gap: 9px;
    font-weight: 400;
    font-size: 26px;
    letter-spacing: 1px;
    line-height: 1;
  }
  .brand__dot {
    width: 10px; height: 10px;
    border-radius: 50%;
    background: var(--ink);
  }
  .brand__tagline {
    margin-top: 8px;
    font-weight: 600;
    font-size: 7.5px;
    letter-spacing: 2.6px;
    text-transform: uppercase;
    color: var(--ink-soft);
  }
  .card--front .brand { top: 92px; }
  .card--back .brand { top: 82px; }

  .person {
    position: absolute;
    left: 0; right: 0;
    top: 178px;
  }
  .person__name {
    font-family: "Yellowtail", "Brush Script MT", cursive;
    font-size: 64px;
    line-height: 1.05;
    color: var(--ink);
  }
  .person__company {
    margin-top: 4px;
    font-weight: 600;
    font-size: 13px;
    letter-spacing: 3px;
    color: var(--accent);
    text-transform: uppercase;
  }

  .contact {
    position: absolute;
    left: 0; right: 0;
    top: 178px;
    list-style: none;
    color: var(--ink-soft);
    font-size: 15.5px;
    font-weight: 400;
    text-transform: uppercase;
  }
  .contact li { height: 33px; line-height: 33px; }
</style>
</head>
<body>
  <section class="card card--front" aria-label="Card front">
    <div class="brand">
      <div class="brand__name"><span class="brand__dot"></span>Ovamir Capital</div>
      <div class="brand__tagline">Building Strength Through Capital</div>
    </div>
    <div class="person">
      <div class="person__name">Glen Ovamir</div>
      <div class="person__company">Ovamir Capital</div>
    </div>
  </section>

  <section class="card card--back" aria-label="Card back">
    <div class="brand">
      <div class="brand__name">Ovamir Capital</div>
      <div class="brand__tagline">Building Strength Through Capital</div>
    </div>
    <ul class="contact">
      <li>630-555-0192</li>
      <li>glenovamir@pvt.insure</li>
      <li>1470 N Thornwick Rd, Suite 210 | Geneva, IL 60134</li>
    </ul>
  </section>
</body>
</html>
```